Webdesign for a Bikeshop in Innsbruck (female audience)

To obtain my master's degree, I am conducting a study in the field of web design as part of my master thesis. All submitted designs will therefore be used for study purposes. In order to achieve a homogeneous group, I would like to encourage not only male but also female web designers to submit a design. All submitted designs will be used anonymously for the study and therefore do not allow any conclusions to be drawn about your person. Since this is a contest, the winner will be chosen randomly from all serious submissions. I would be really happy if you would support me in my study. I think the results could be very informative and also useful for your further work (I won't go into more detail here as it could skew the results - but once the contest is over, feel free to contact me. Of course I will also provide you with my results as soon as my work is finished). Below you will find a fictitious usecase and a description of what the website should include:

The company Pedalhaus Norvik is planning to relaunch its own website and would like to present itself primarily as a competent and leading consultant in the field of cargo bikes. The design should appeal to a broad audience and embody an urban lifestyle. In any case, the website should include a landing page, a product overview page and a product details page. The company also wants to appeal mainly to a FEMALE target group. You only design the website. So don't worry about hardware or software limitations, just create the best bike store design you can.

As it is fictitious, I can't offer any materials. A logo is not necessary, you can use a placeholder or whatever you have access to. If you need any inspring websites feel free to contact me.

Target Market(s)

female users

Number of Pages Required

1 page

Requirements
Must have
• landing page, product overview page, product details page
Should not have
• online shop

```html
<!DOCTYPE html>
<html lang="en">
<head>
<meta charset="utf-8">
<title>Pedalhaus Norvik – Cargo Bikes for Females</title>
<link href="https://fonts.googleapis.com/css2?family=Poppins:wght@400;500;600;700;800&display=swap" rel="stylesheet">
<style>
:root{
  --ink:#2b2b2b;
  --muted:#4a4a4a;
  --cyan:#3fdcf7;
  --teal:#2aa3cf;
  --icon-blue:#2f9fe0;
  --white:#ffffff;
  --sky:#c2e7f7;
  --ocean:#3a9ed3;
  --card-grey:#e6e6e6;
  --star:#f7c21b;
}
*{box-sizing:border-box;margin:0;padding:0}
html,body{width:1200px;height:3627px;overflow:hidden}
body{position:relative;background:var(--white);font-family:'Poppins',sans-serif;color:var(--ink)}

/* header */
.site-header{position:absolute;left:0;top:0;width:1200px;height:90px;background:var(--white)}
.brand{position:absolute;left:64px;top:28px;display:flex;align-items:center;gap:12px;font-size:27px;font-weight:500;color:#333;letter-spacing:.2px}
.brand-mark{width:22px;height:22px;background:#333}
.main-nav{position:absolute;top:34px;left:0;width:1200px;font-size:17px;color:#333}
.main-nav a{position:absolute;color:inherit;text-decoration:none;white-space:nowrap}
.main-nav a.active{font-weight:600}

/* hero */
.hero{position:absolute;left:0;top:90px;width:1200px;height:763px;background:linear-gradient(100deg,#8a8f86 0%,#5d625f 30%,#3c3a39 60%,#2f2c2b 100%)}
.hero-photo{position:absolute;inset:0;background:linear-gradient(180deg,rgba(255,255,255,0) 55%,rgba(70,90,50,.55) 100%)}
.hero-title{position:absolute;right:60px;top:126px;width:600px;height:200px;color:var(--white);line-height:1}
.hero-title .light{font-size:80px;font-weight:500;position:absolute;right:0;top:0;white-space:nowrap}
.hero-title .bold{font-size:80px;font-weight:800;position:absolute;right:0;top:108px;white-space:nowrap}
.hero-sub{position:absolute;right:57px;top:344px;font-size:29px;color:var(--cyan);font-weight:500;white-space:nowrap}
.btn-pill{display:flex;align-items:center;justify-content:center;background:var(--cyan);color:var(--white);border-radius:32px;font-weight:500;text-decoration:none}
.hero-cta{position:absolute;left:960px;top:413px;width:180px;height:62px;font-size:20px}
.hero-text{position:absolute;right:66px;top:510px;width:390px;text-align:right;font-size:16.5px;line-height:27px;color:var(--white);font-weight:500}

/* featured */
.section-title{font-weight:700;letter-spacing:4px;color:var(--ink)}
.featured-title{position:absolute;left:0;width:1200px;top:913px;text-align:center;font-size:38px}
.product{position:absolute;top:1002px;width:281px;height:445px;text-align:center}
.product.raised{background:var(--white);box-shadow:0 2px 8px rgba(0,0,0,.2)}
.product-photo{width:281px;height:279px;box-shadow:0 1px 5px rgba(0,0,0,.25)}
.product-name{margin-top:28px;font-size:17px;font-weight:600;color:var(--teal)}
.product-price{margin-top:12px;font-size:17px;font-weight:500;color:#555}
.select-btn{display:inline-block;margin-top:16px;border:1.5px solid var(--teal);border-radius:14px;padding:5px 11px;font-size:9px;font-weight:600;color:var(--teal)}
.view-more{position:absolute;left:527px;top:1497px;width:180px;height:62px;font-size:19px}

/* about */
.about-photo-a{position:absolute;left:128px;top:1639px;width:389px;height:389px;background:linear-gradient(160deg,#2c5fb4 0%,#3c76c4 40%,#b47f58 70%,#d89a64 100%)}
.about-photo-b{position:absolute;left:306px;top:1802px;width:285px;height:286px;border:7px solid var(--white);background:linear-gradient(140deg,#8ea4b8 0%,#53667a 45%,#a2743f 75%,#5d8a47 100%)}
.about-title{position:absolute;left:639px;top:1654px;font-size:38px}
.about-text{position:absolute;left:641px;width:420px;font-size:14.5px;line-height:29px;letter-spacing:.6px;color:var(--muted)}
.read-more{position:absolute;left:644px;top:2030px;font-size:16px;font-weight:600;letter-spacing:.8px;color:#333}

/* ride */
.ride-photo{position:absolute;left:490px;top:2180px;width:710px;height:467px;background:linear-gradient(90deg,rgba(255,255,255,1) 0%,rgba(225,215,205,.7) 18%,#b8a898 40%,#c98c3a 65%,#6b5a4c 100%)}
.ride-title{position:absolute;left:153px;top:2203px;font-size:36px;font-weight:800;letter-spacing:3px}
.perk{position:absolute;left:160px;display:flex;align-items:center;gap:16px;width:380px;font-size:14.5px;line-height:25px;color:#222}
.perk svg{flex:none}

/* quote */
.quote{position:absolute;left:180px;top:2726px;width:840px;text-align:center;font-size:23.5px;line-height:36.5px;color:#222}
.quote-author{position:absolute;left:0;width:1200px;top:2897px;text-align:center;font-size:21px;color:#222}

/* clients */
.clients-photo{position:absolute;left:0;top:2980px;width:449px;height:394px;background:linear-gradient(170deg,#8b9186 0%,#5a5b57 40%,#8c5f48 70%,#a36b4f 100%)}
.clients-panel{position:absolute;left:449px;top:2980px;width:751px;height:394px;background:linear-gradient(180deg,#3ea3d8 0%,#3996c9 60%,#3fa1d6 100%)}
.clients-title{position:absolute;left:0;width:751px;top:42px;text-align:center;font-size:30px;font-weight:700;color:var(--white);letter-spacing:.5px}
.client-card{position:absolute;top:157px;width:219px;height:154px;background:var(--card-grey);border-radius:4px;text-align:center}
.client-avatar{position:absolute;left:63px;top:-57px;width:93px;height:93px;border-radius:50%;border:3px solid var(--ocean);background:radial-gradient(circle at 50% 45%,#e2b894 0%,#b98557 60%,#7a5238 100%)}
.client-stars{position:absolute;left:0;width:219px;top:52px;display:flex;justify-content:center;gap:18px}
.client-name{position:absolute;left:0;width:219px;top:76px;font-size:8px;font-weight:500;color:#333}
.client-quote{position:absolute;left:15px;top:96px;width:189px;height:46px;background:#dadada;border-radius:3px;padding:5px 6px;font-size:6px;line-height:8.5px;color:#888}

/* action */
.action{position:absolute;left:0;top:3374px;width:1200px;height:253px;background:var(--sky)}
.action-title{position:absolute;left:0;width:1230px;top:50px;text-align:center;font-size:25px;font-weight:400;color:#444;letter-spacing:.5px}
.action-btn{position:absolute;top:115px;width:172px;height:42px;background:var(--white);color:var(--teal);display:flex;align-items:center;justify-content:center;font-size:19px;text-decoration:none}
.copyright{position:absolute;left:0;width:1200px;top:193px;text-align:center;font-size:12.5px;color:#666;letter-spacing:.3px}
</style>
</head>
<body>

<header class="site-header">
  <div class="brand"><span class="brand-mark"></span><span>Pedalhaus Norvik</span></div>
  <nav class="main-nav">
    <a class="active" style="left:584px">HOME</a>
    <a style="left:689px">ABOUT US</a>
    <a style="left:829px">SHOP</a>
    <a style="left:919px">CONTACT US</a>
  </nav>
</header>

<section class="hero">
  <div class="hero-photo" role="img" aria-label="Woman riding a cargo bike with two smiling children in the front box"></div>
  <h1 class="hero-title">
    <span class="light">Pedalhaus</span>
    <span class="bold">NORVIK</span>
  </h1>
  <p class="hero-sub">CARGO BIKES FOR FEMALES</p>
  <a class="btn-pill hero-cta">GET STARTED</a>
  <p class="hero-text">We manufacture cargo bikes and accessories for safe driving with 1-4 kids. Fjordlings are designed, welded, sewn and assembled.</p>
</section>

<h2 class="section-title featured-title">FEATURED</h2>

<article class="product" style="left:160px">
  <div class="product-photo" role="img" aria-label="Woman on a cargo bike with a child in the wooden box" style="background:linear-gradient(180deg,#d9dde0 0%,#c9c4bb 55%,#a58b6a 100%)"></div>
  <h3 class="product-name">FEMALE CARGO CYCLE 1</h3>
  <p class="product-price">€2.498,00 INC. 23% VAT</p>
  <span class="select-btn">SELECT OPTIONS</span>
</article>
<article class="product" style="left:461px">
  <div class="product-photo" role="img" aria-label="Woman pushing a cargo bike with a child and a dog aboard" style="background:linear-gradient(180deg,#e4e6e8 0%,#a9b1b8 50%,#6d6a64 100%)"></div>
  <h3 class="product-name">FEMALE CARGO CYCLE 2</h3>
  <p class="product-price">€2.498,00 INC. 23% VAT</p>
  <span class="select-btn">SELECT OPTIONS</span>
</article>
<article class="product raised" style="left:759px">
  <div class="product-photo" role="img" aria-label="Woman with a cargo bike loaded with shopping on a city street" style="background:linear-gradient(180deg,#8a8275 0%,#6f6a62 45%,#8c3b2c 75%,#555049 100%)"></div>
  <h3 class="product-name">FEMALE CARGO CYCLE 3</h3>
  <p class="product-price">€2.498,00 INC. 23% VAT</p>
  <span class="select-btn">SELECT OPTIONS</span>
</article>

<a class="btn-pill view-more">VIEW MORE</a>

<div class="about-photo-a" role="img" aria-label="Old town column and colourful houses in front of blue mountains"></div>
<div class="about-photo-b" role="img" aria-label="Woman riding a cargo bike with a child and a dog"></div>
<h2 class="section-title about-title">ABOUT</h2>
<p class="about-text" style="top:1727px">Lorem ipsum dolor sit amet, consectetur adipiscing elit, sed do eiusmod tempor incididunt ut labore et dolore magna aliqua. Quis ipsum suspendisse ultrices gravida.</p>
<p class="about-text" style="top:1870px">Lorem ipsum dolor sit amet, consectetur adipiscing elit, sed do eiusmod tempor incididunt ut labore et dolore magna aliqua. Quis ipsum suspendisse ultrices gravida. Risus commodo viverra maecenas accumsan lacus vel facilisis.</p>
<a class="read-more">READ MORE</a>

<section>
  <div class="ride-photo" role="img" aria-label="Mother leaning over two laughing children in a cargo bike box"></div>
  <h2 class="ride-title">100% YOUR RIDE</h2>
  <div class="perk" style="top:2277px">
    <svg width="40" height="40" viewBox="0 0 40 40" aria-hidden="true"><circle cx="20" cy="20" r="19" fill="#e8f3fb"/><circle cx="20" cy="20" r="15" fill="var(--icon-blue)"/><circle cx="14" cy="24" r="3.2" fill="none" stroke="#fff" stroke-width="1.6"/><circle cx="26" cy="24" r="3.2" fill="none" stroke="#fff" stroke-width="1.6"/><path d="M14 24l4-7h6l2 7M18 17l-1-2" fill="none" stroke="#fff" stroke-width="1.6"/></svg>
    <span>Lorem Ipsum is simply dummy text of the printing and typesetting industry.</span>
  </div>
  <div class="perk" style="top:2346px">
    <svg width="40" height="40" viewBox="0 0 40 40" aria-hidden="true"><circle cx="20" cy="20" r="19" fill="#e8f3fb"/><circle cx="20" cy="20" r="15" fill="var(--icon-blue)"/><circle cx="14" cy="24" r="3.2" fill="none" stroke="#fff" stroke-width="1.6"/><circle cx="26" cy="24" r="3.2" fill="none" stroke="#fff" stroke-width="1.6"/><path d="M14 24l4-7h6l2 7M18 17l-1-2" fill="none" stroke="#fff" stroke-width="1.6"/></svg>
    <span>Lorem Ipsum is simply dummy text of the printing and typesetting industry.</span>
  </div>
  <div class="perk" style="top:2421px">
    <svg width="40" height="40" viewBox="0 0 40 40" aria-hidden="true"><circle cx="20" cy="20" r="19" fill="#e8f3fb"/><circle cx="20" cy="20" r="15" fill="var(--icon-blue)"/><circle cx="14" cy="24" r="3.2" fill="none" stroke="#fff" stroke-width="1.6"/><circle cx="26" cy="24" r="3.2" fill="none" stroke="#fff" stroke-width="1.6"/><path d="M14 24l4-7h6l2 7M18 17l-1-2" fill="none" stroke="#fff" stroke-width="1.6"/></svg>
    <span>Lorem Ipsum is simply dummy text of the printing.</span>
  </div>
  <div class="perk" style="top:2491px">
    <svg width="40" height="40" viewBox="0 0 40 40" aria-hidden="true"><circle cx="20" cy="20" r="19" fill="#e8f3fb"/><circle cx="20" cy="20" r="15" fill="var(--icon-blue)"/><circle cx="14" cy="24" r="3.2" fill="none" stroke="#fff" stroke-width="1.6"/><circle cx="26" cy="24" r="3.2" fill="none" stroke="#fff" stroke-width="1.6"/><path d="M14 24l4-7h6l2 7M18 17l-1-2" fill="none" stroke="#fff" stroke-width="1.6"/></svg>
    <span>Lorem Ipsum is simply dummy text of the printing and typesetting industry.</span>
  </div>
  <div class="perk" style="top:2567px">
    <svg width="40" height="40" viewBox="0 0 40 40" aria-hidden="true"><circle cx="20" cy="20" r="19" fill="#e8f3fb"/><circle cx="20" cy="20" r="15" fill="var(--icon-blue)"/><circle cx="14" cy="24" r="3.2" fill="none" stroke="#fff" stroke-width="1.6"/><circle cx="26" cy="24" r="3.2" fill="none" stroke="#fff" stroke-width="1.6"/><path d="M14 24l4-7h6l2 7M18 17l-1-2" fill="none" stroke="#fff" stroke-width="1.6"/></svg>
    <span>Lorem Ipsum is simply dummy text of the printing.</span>
  </div>
</section>

<blockquote class="quote">“Lorem Ipsum is simply dummy text of the printing and typesetting industry. Lorem Ipsum has been the industry's standard dummy text ever since the 1500s, when an unknown printer took a galley of type and scrambled it to make a type specimen book. ”</blockquote>
<p class="quote-author">-Anonomous</p>

<section>
  <div class="clients-photo" role="img" aria-label="Black cargo bike with covered box parked on brick pavement"></div>
  <div class="clients-panel">
    <h2 class="clients-title">SATISFIED CLIENTS</h2>

    <div class="client-card" style="left:33px">
      <div class="client-avatar" role="img" aria-label="Customer portrait"></div>
      <div class="client-stars">
        <svg width="13" height="13" viewBox="0 0 24 24"><path d="M12 2l3 7h7l-5.5 4.5 2 7.5L12 16.5 5.5 21l2-7.5L2 9h7z" fill="var(--star)"/></svg>
        <svg width="13" height="13" viewBox="0 0 24 24"><path d="M12 2l3 7h7l-5.5 4.5 2 7.5L12 16.5 5.5 21l2-7.5L2 9h7z" fill="var(--star)"/></svg>
        <svg width="13" height="13" viewBox="0 0 24 24"><path d="M12 2l3 7h7l-5.5 4.5 2 7.5L12 16.5 5.5 21l2-7.5L2 9h7z" fill="var(--star)"/></svg>
        <svg width="13" height="13" viewBox="0 0 24 24"><path d="M12 2l3 7h7l-5.5 4.5 2 7.5L12 16.5 5.5 21l2-7.5L2 9h7z" fill="var(--star)"/></svg>
        <svg width="13" height="13" viewBox="0 0 24 24"><path d="M12 2l3 7h7l-5.5 4.5 2 7.5L12 16.5 5.5 21l2-7.5L2 9h7z" fill="var(--star)"/></svg>
      </div>
      <p class="client-name">CUSTOMER NAME</p>
      <p class="client-quote">Lorem ipsum is simply dummy text of the printing and typesetting industry. Lorem ipsum has been the standard dummy text since the 1500s.</p>
    </div>

    <div class="client-card" style="left:270px">
      <div class="client-avatar" role="img" aria-label="Customer portrait" style="background:radial-gradient(circle at 50% 45%,#e6c2a4 0%,#9b6845 60%,#5c3a26 100%)"></div>
      <div class="client-stars">
        <svg width="13" height="13" viewBox="0 0 24 24"><path d="M12 2l3 7h7l-5.5 4.5 2 7.5L12 16.5 5.5 21l2-7.5L2 9h7z" fill="var(--star)"/></svg>
        <svg width="13" height="13" viewBox="0 0 24 24"><path d="M12 2l3 7h7l-5.5 4.5 2 7.5L12 16.5 5.5 21l2-7.5L2 9h7z" fill="var(--star)"/></svg>
        <svg width="13" height="13" viewBox="0 0 24 24"><path d="M12 2l3 7h7l-5.5 4.5 2 7.5L12 16.5 5.5 21l2-7.5L2 9h7z" fill="var(--star)"/></svg>
        <svg width="13" height="13" viewBox="0 0 24 24"><path d="M12 2l3 7h7l-5.5 4.5 2 7.5L12 16.5 5.5 21l2-7.5L2 9h7z" fill="var(--star)"/></svg>
        <svg width="13" height="13" viewBox="0 0 24 24"><path d="M12 2l3 7h7l-5.5 4.5 2 7.5L12 16.5 5.5 21l2-7.5L2 9h7z" fill="var(--star)"/></svg>
      </div>
      <p class="client-name">CUSTOMER NAME</p>
      <p class="client-quote">Lorem ipsum is simply dummy text of the printing and typesetting industry. Lorem ipsum has been the standard dummy text since the 1500s.</p>
    </div>

    <div class="client-card" style="left:508px">
      <div class="client-avatar" role="img" aria-label="Customer portrait" style="background:radial-gradient(circle at 50% 45%,#e7c3a6 0%,#6b4a3a 60%,#2a1f1c 100%)"></div>
      <div class="client-stars">
        <svg width="13" height="13" viewBox="0 0 24 24"><path d="M12 2l3 7h7l-5.5 4.5 2 7.5L12 16.5 5.5 21l2-7.5L2 9h7z" fill="var(--star)"/></svg>
        <svg width="13" height="13" viewBox="0 0 24 24"><path d="M12 2l3 7h7l-5.5 4.5 2 7.5L12 16.5 5.5 21l2-7.5L2 9h7z" fill="var(--star)"/></svg>
        <svg width="13" height="13" viewBox="0 0 24 24"><path d="M12 2l3 7h7l-5.5 4.5 2 7.5L12 16.5 5.5 21l2-7.5L2 9h7z" fill="var(--star)"/></svg>
        <svg width="13" height="13" viewBox="0 0 24 24"><path d="M12 2l3 7h7l-5.5 4.5 2 7.5L12 16.5 5.5 21l2-7.5L2 9h7z" fill="var(--star)"/></svg>
        <svg width="13" height="13" viewBox="0 0 24 24"><path d="M12 2l3 7h7l-5.5 4.5 2 7.5L12 16.5 5.5 21l2-7.5L2 9h7z" fill="var(--star)"/></svg>
      </div>
      <p class="client-name">CUSTOMER NAME</p>
      <p class="client-quote">Lorem ipsum is simply dummy text of the printing and typesetting industry. Lorem ipsum has been the standard dummy text since the 1500s.</p>
    </div>
  </div>
</section>

<footer class="action">
  <h2 class="action-title">TAKE ACTION</h2>
  <a class="action-btn" style="left:318px">SHOP NOW</a>
  <a class="action-btn" style="left:518px">INQUIRE</a>
  <a class="action-btn" style="left:727px">CONTACT</a>
  <p class="copyright">COPYRIGHTS2022@PEDALHAUS NORVIK. ALL RIGHTS RECEIVED</p>
</footer>

</body>
</html>
```